Business Cards for a law firm

Business cards for our law firm. Use our silhoette logo and OAK HARBOR - check our website (www.oakharbor-legal.com)

Contact Information for Business Card

our silhouette logo, OAK HARBOR, 800-555-0147, Dorian Kestrup, dorian@oakharbor-legal.com

Requirements
Must have
• our silhouette logo, OAK HARBOR, 800-555-0147, Dorian Kestrup, dorian@oakharbor-legal.com

```html
<!DOCTYPE html>
<html lang="en">
<head>
<meta charset="utf-8">
<title>Oak Harbor – Business Cards</title>
<link href="https://fonts.googleapis.com/css2?family=Inter:wght@400;500;600&display=swap" rel="stylesheet">
<style>
  :root {
    --backdrop: #808080;
    --card-dark: #0f1a2a;
    --card-light: #ffffff;
    --emboss: #3b4454;
    --navy: #1f3272;
    --ink: #1c1c1c;
    --grey-text: #555555;
    --tagline: #6f6f6f;
    --title: #6a63a0;
    --divider: #c9c9c9;
  }
  * { margin: 0; padding: 0; box-sizing: border-box; }
  html, body { width: 1200px; height: 1200px; overflow: hidden; }
  body {
    background: var(--backdrop);
    font-family: "Inter", sans-serif;
    position: relative;
  }
  .card {
    position: absolute;
    left: 179px;
    width: 861px;
    height: 495px;
  }
  .card--front { top: 84px; background: var(--card-dark); }
  .card--back { top: 622px; background: var(--card-light); }

  /* Front */
  .front-mark {
    position: absolute;
    left: 330px; top: 286px;
    width: 38px; height: 38px;
    background: var(--emboss);
  }
  .front-name {
    position: absolute;
    left: 386px; top: 278px;
    font-size: 48px; font-weight: 600;
    letter-spacing: 5px;
    color: var(--emboss);
    line-height: 1;
  }
  .front-tagline {
    position: absolute;
    left: 470px; top: 344px;
    font-size: 24px; font-weight: 500;
    letter-spacing: 5px;
    color: var(--emboss);
    line-height: 1;
  }

  /* Back */
  .back-mark {
    position: absolute;
    left: 56px; top: 205px;
    width: 30px; height: 30px;
    background: var(--navy);
  }
  .back-name {
    position: absolute;
    left: 100px; top: 223px;
    font-size: 28px; font-weight: 600;
    letter-spacing: 2px;
    color: var(--navy);
    line-height: 1;
  }
  .back-tagline {
    position: absolute;
    left: 141px; top: 256px;
    font-size: 18px; font-weight: 500;
    letter-spacing: 1.5px;
    color: var(--tagline);
    line-height: 1;
  }
  .divider {
    position: absolute;
    left: 425px; top: 162px;
    width: 1.5px; height: 205px;
    background: var(--divider);
  }
  .contact {
    position: absolute;
    left: 439px; top: 150px;
  }
  .person-name {
    font-size: 34px; font-weight: 600;
    color: var(--ink);
    line-height: 1.1;
    letter-spacing: 0.5px;
  }
  .person-title {
    font-size: 19px; font-weight: 400;
    color: var(--title);
    letter-spacing: 1px;
    line-height: 1.1;
    margin-top: 2px;
  }
  .address {
    margin-top: 14px;
    font-size: 19px; font-weight: 500;
    letter-spacing: 2.4px;
    color: var(--grey-text);
    line-height: 25px;
  }
  .contact-list { list-style: none; margin-top: 14px; }
  .contact-item {
    display: flex; align-items: center;
    font-size: 19.5px; font-weight: 500;
    letter-spacing: 2.6px;
    color: var(--ink);
    height: 31px;
  }
  .contact-icon {
    width: 22px; height: 22px;
    margin-right: 10px;
    flex: none;
  }
</style>
</head>
<body>
  <section class="card card--front" aria-label="Card front">
    <div class="front-mark"></div>
    <div class="front-name">OAK HARBOR</div>
    <div class="front-tagline">INJURY ATTORNEYS</div>
  </section>

  <section class="card card--back" aria-label="Card back">
    <div class="back-mark"></div>
    <div class="back-name">OAK HARBOR</div>
    <div class="back-tagline">INJURY ATTORNEYS</div>

    <div class="divider"></div>

    <div class="contact">
      <h1 class="person-name">Dorian Kestrup</h1>
      <p class="person-title">President/Owner</p>
      <p class="address">1420 Harbor View Dr #310,<br>Port Alder, CA 90415</p>
      <ul class="contact-list">
        <li class="contact-item">
          <svg class="contact-icon" viewBox="0 0 22 22" aria-hidden="true">
            <rect width="22" height="22" fill="#1f3272"/>
            <path d="M7 4.5c1 0 1.6 2.6 1.6 3.2 0 .6-1 1-1 1.6 0 1.5 2.6 5.2 4 5.2.6 0 1-1 1.6-1 .6 0 3 1 3 2 0 1-1.5 2.2-2.5 2.2C9.5 17.7 4.3 11 4.3 7.3c0-1 1.6-2.8 2.7-2.8z" fill="#fff"/>
          </svg>
          800-555-0147
        </li>
        <li class="contact-item">
          <svg class="contact-icon" viewBox="0 0 22 22" aria-hidden="true">
            <rect width="22" height="22" fill="#1f3272"/>
            <rect x="4" y="6" width="14" height="10" fill="none" stroke="#fff" stroke-width="1.5"/>
            <path d="M4 6l7 6 7-6M4 16l5-5M18 16l-5-5" fill="none" stroke="#fff" stroke-width="1.3"/>
          </svg>
          dorian@oakharbor-legal.com
        </li>
        <li class="contact-item">
          <svg class="contact-icon" viewBox="0 0 22 22" aria-hidden="true">
            <rect width="22" height="22" fill="#1f3272"/>
            <circle cx="11" cy="11" r="6.5" fill="none" stroke="#fff" stroke-width="1.5"/>
            <path d="M4.5 11h13M11 4.5c-3 3.5-3 9.5 0 13M11 4.5c3 3.5 3 9.5 0 13" fill="none" stroke="#fff" stroke-width="1.2"/>
          </svg>
          oakharbor-legal.com
        </li>
      </ul>
    </div>
  </section>
</body>
</html>
```